Buch-/eBook-Cover für Buch zum Thema Verkauf auf Verkando
Zielgruppe
E-Commerce Plattform für Verkando Händler
Aufgabenstellung
Das Buch soll eine umfassende Anleitung für den Verkauf auf Verkando abbilden. Als Buchcover war die Überlegung, dieses wie ein typisches Verkando Paket aussehen zu lassen (braunes Paketdesign mit typischen Verkando Farben & Elementen). Es sollte jedoch kein Verkando Logo oder rechtlich geschützte Elemente enthalten sein.
Auf dem Cover sollen folgende Texte verbaut sein:
Titel : DAS TOPLISTEN WERK
Untertitel: In 99 Etappen zum Toplisten-Hit auf Verkando
Authoren: Jonas Weitbrecht, Lukas Dornfeld, Tobias Quernheim
Webseite: vkd-profis.de
Beschreibung (optional): Eine vollumfängliche Anleitung rund um das Thema 'Verkando VLS'. Von der Unternehmensgründung, über die Produktrecherche bis hin zur Markteinführung deines ersten Produktes.

```html
<!DOCTYPE html>
<html lang="de">
<head>
<meta charset="utf-8">
<title>Das Toplisten Werk – Buchcover</title>
<link rel="stylesheet" href="https://fonts.googleapis.com/css2?family=Bebas+Neue&family=Roboto+Condensed:wght@400;700&display=swap">
<style>
  :root {
    --cardboard: #ebb77a;
    --cardboard-light: #efbf85;
    --cardboard-shade: #d9a66c;
    --tape-strip: #e2ad70;
    --fold: #a8733f;
    --edge: #9c6a3a;
    --tape-black: #141210;
    --tape-black-soft: #1c1915;
    --title-white: #ffffff;
    --subtitle-blue: #0a9be0;
    --ink: #241b13;
    --label-white: #ffffff;
    --label-ink: #3a3a3a;
  }
  * { margin: 0; padding: 0; box-sizing: border-box; }
  html, body { width: 750px; height: 1200px; overflow: hidden; background: #ffffff; }
  .cover {
    position: relative;
    width: 750px;
    height: 1200px;
    overflow: hidden;
    background: linear-gradient(180deg, var(--cardboard-light) 0%, var(--cardboard) 50%, var(--cardboard-light) 100%);
    font-family: "Bebas Neue", sans-serif;
  }
  .cover-shapes { position: absolute; inset: 0; }
  .title {
    position: absolute;
    left: 78px;
    color: var(--title-white);
    line-height: 1;
    letter-spacing: 0.5px;
  }
  .title-small { top: 336px; font-size: 64px; }
  .title-main { top: 397px; font-size: 126px; }
  .title-last { top: 506px; font-size: 126px; }
  .subtitle {
    position: absolute;
    left: 305px;
    top: 512px;
    color: var(--subtitle-blue);
    font-size: 44px;
    line-height: 50px;
    letter-spacing: 0.3px;
  }
  .website {
    position: absolute;
    left: 37px;
    top: 1129px;
    color: var(--ink);
    font-size: 37px;
    line-height: 1;
  }
  .sender-label {
    position: absolute;
    left: 477px;
    top: 997px;
    width: 252px;
    height: 150px;
    background: var(--label-white);
    transform: rotate(-0.4deg);
    box-shadow: 0 1px 2px rgba(0,0,0,0.15);
    padding: 24px 0 0 16px;
    font-family: "Roboto Condensed", sans-serif;
    color: var(--label-ink);
  }
  .sender-heading { font-weight: 700; font-size: 17px; margin-bottom: 10px; }
  .sender-name { font-size: 15px; line-height: 18px; }
</style>
</head>
<body>
<main class="cover">
  <svg class="cover-shapes" width="750" height="1200" viewBox="0 0 750 1200" aria-hidden="true">
    <!-- box edges -->
    <rect x="0" y="0" width="750" height="5" fill="var(--edge)"/>
    <rect x="0" y="1194" width="750" height="6" fill="var(--edge)"/>
    <rect x="0" y="0" width="3" height="1200" fill="var(--cardboard-shade)"/>
    <rect x="747" y="0" width="3" height="1200" fill="var(--cardboard-shade)"/>
    <!-- vertical packing tape strip and fold -->
    <rect x="295" y="0" width="160" height="1200" fill="var(--tape-strip)"/>
    <rect x="371" y="0" width="6" height="1200" fill="var(--fold)"/>
    <!-- black tape -->
    <polygon points="0,323 642,342 624,446 0,497" fill="var(--tape-black-soft)"/>
    <polygon points="47,445 750,445 750,622 31,622" fill="var(--tape-black)"/>
    <!-- this side up arrows -->
    <g fill="var(--ink)">
      <polygon points="74,931 92,911 110,931"/>
      <rect x="87" y="929" width="11" height="165"/>
      <polygon points="121,931 139,911 157,931"/>
      <rect x="134" y="929" width="11" height="165"/>
      <rect x="60" y="1102" width="111" height="10"/>
    </g>
  </svg>

  <h1>
    <span class="title title-small">Das</span>
    <span class="title title-main">Toplisten</span>
    <span class="title title-last">Werk</span>
  </h1>
  <p class="subtitle">In 99 Etappen zum<br>Toplisten-Hit auf Verkando</p>

  <p class="website">vkd-profis.de</p>

  <section class="sender-label">
    <p class="sender-heading">Absender:</p>
    <p class="sender-name">Jonas Weitbrecht</p>
    <p class="sender-name">Lukas Dornfeld</p>
    <p class="sender-name">Tobias Quernheim</p>
  </section>
</main>
</body>
</html>
```